Contemporary Media Company with Logo Needs Business Card Design

Need a modern card design for a full service digital media company using the logo included. Also want the info below on the card. Probably list the services on the card back to save space for the front. Want something contemporary to impress prospective clients. You may want to submit both a somewhat more conservative design, and then a more wild one.
General Info: (this phrase need not be on the card)
Tod Parvin
Founder and CEO
949-628-4513
tod@lumavantstudio.example
lumavantstudio.example
Services: (this word need not be on the card)
Content & Experience Strategy
Brand Development
Search Engine Optimization
Website Design
Website Operation
Social Media Integration
Complete Video Solutions
Industry/Entity Type
Business
Contact Information for Business Card
Tod Parvin
Founder and CEO
949-628-4513
tod@lumavantstudio.example
lumavantstudio.example
Brand Development
Website Design
Website Operation
Social Media Integration
Complete Video Solutions
Look and feel

```html
<!DOCTYPE html>
<html lang="en">
<head>
<meta charset="utf-8">
<title>Lumavant Studio – Business Card</title>
<link rel="stylesheet" href="https://fonts.googleapis.com/css2?family=Source+Sans+3:wght@300;400&display=swap">
<style>
  :root {
    --ink: #0c0c0c;
    --ink-soft: #1c1c1c;
    --orange: #e06a22;
    --orange-light: #f08a3a;
    --grey: #b9b9b9;
    --white: #ffffff;
    --backdrop: #ece8e3;
  }
  * { box-sizing: border-box; margin: 0; padding: 0; }
  html, body {
    width: 1200px; height: 902px; overflow: hidden;
    background: var(--backdrop);
    font-family: "Source Sans 3", "Myriad Pro", sans-serif;
  }
  .sheet {
    width: 1200px; height: 902px;
    display: flex; flex-direction: column; align-items: center; justify-content: center; gap: 40px;
  }
  .card {
    position: relative; width: 700px; height: 400px; overflow: hidden;
    border-radius: 6px; box-shadow: 0 8px 24px rgba(0,0,0,.18);
  }

  /* Back */
  .card-back { background: linear-gradient(160deg, var(--ink-soft), var(--ink) 60%); }
  .services { position: absolute; left: 70px; top: 96px; list-style: none; }
  .services li {
    display: flex; align-items: center; gap: 16px;
    color: var(--grey); font-weight: 300; font-size: 24px; line-height: 31px;
  }
  .services li::before {
    content: ""; width: 9px; height: 9px; background: var(--orange); flex: none;
  }
  .back-accent {
    position: absolute; right: 70px; top: 80px; width: 170px; height: 120px;
    background: var(--orange); opacity: .22;
  }

  /* Front */
  .card-front { background: var(--orange); }
  .front-band { position: absolute; inset: 0; }
  .brand {
    position: absolute; left: 190px; top: 92px;
    display: flex; align-items: center; gap: 18px;
  }
  .brand-mark { width: 40px; height: 40px; background: var(--orange); }
  .brand-name {
    color: var(--grey); font-weight: 300; font-size: 52px;
    letter-spacing: 4px; text-transform: uppercase;
  }
  .holder { position: absolute; left: 60px; bottom: 52px; color: var(--white); }
  .holder-name { font-size: 30px; font-weight: 400; }
  .holder-title { font-size: 22px; font-weight: 300; margin-top: 4px; }
  .divider {
    position: absolute; left: 330px; bottom: 46px; width: 1.5px; height: 110px;
    background: rgba(255,255,255,.75);
  }
  .contact { position: absolute; left: 360px; bottom: 66px; list-style: none; }
  .contact li {
    display: flex; align-items: center; gap: 12px;
    color: var(--white); font-size: 19px; font-weight: 400; line-height: 30px;
  }
  .contact svg { width: 16px; height: 16px; flex: none; }
</style>
</head>
<body>
<main class="sheet">
  <section class="card card-back" aria-label="Card back">
    <div class="back-accent"></div>
    <ul class="services">
      <li>Website Design</li>
      <li>Website Operation</li>
      <li>Brand Development</li>
      <li>Social Media Integration</li>
      <li>Complete Video Solutions</li>
      <li>Search Engine Optimization</li>
      <li>Content &amp; Experience Strategy</li>
    </ul>
  </section>

  <section class="card card-front" aria-label="Card front">
    <svg class="front-band" viewBox="0 0 700 400" preserveAspectRatio="none" aria-hidden="true">
      <path d="M0,0 H700 V150 Q420,300 0,215 Z" fill="var(--ink)"/>
    </svg>
    <div class="brand">
      <span class="brand-mark"></span>
      <span class="brand-name">Lumavant Studio</span>
    </div>
    <div class="holder">
      <p class="holder-name">Tod Parvin</p>
      <p class="holder-title">Founder and CEO</p>
    </div>
    <div class="divider"></div>
    <ul class="contact">
      <li>
        <svg viewBox="0 0 16 16"><rect width="16" height="16" rx="2" fill="#fff"/><path d="M5 3.5l2 2-1.2 1.2a6 6 0 0 0 3.5 3.5L10.5 9l2 2-1.5 1.5C7 12.5 3.5 9 3.5 5z" fill="var(--orange)"/></svg>
        949-628-4513
      </li>
      <li>
        <svg viewBox="0 0 16 16"><rect width="16" height="16" rx="2" fill="#fff"/><rect x="3" y="4.5" width="10" height="7" fill="none" stroke="var(--orange)" stroke-width="1.4"/><path d="M3 4.5l5 4 5-4" fill="none" stroke="var(--orange)" stroke-width="1.4"/></svg>
        tod@lumavantstudio.example
      </li>
      <li>
        <svg viewBox="0 0 16 16"><rect width="16" height="16" rx="2" fill="#fff"/><circle cx="8" cy="8" r="4.5" fill="none" stroke="var(--orange)" stroke-width="1.3"/><path d="M3.5 8h9M8 3.5c-2 2.5-2 6.5 0 9M8 3.5c2 2.5 2 6.5 0 9" fill="none" stroke="var(--orange)" stroke-width="1"/></svg>
        www.lumavantstudio.example
      </li>
    </ul>
  </section>
</main>
</body>
</html>
```